A reimagined website for a cross-border tax firm

There are two aspects to this project for Brindlemoor Tax Advisory:
1) I need a logo update to accommodate increasing focus and specialization in my business. The byline under the name “Brindlemoor Tax Advisory” needs to change:
ORIGINAL: TAX SUPPORT FOR PUBLIC ACCOUNTING FIRMS
REVISED: CROSS-BORDER TAX SERVICES • U.S. & CANADA
2) I need a website “refresh” (see current website at www.levyhelpdesk.example) based on this logo – a new vision for a website with greater clarity, focus and organization. It should represent a re-envisioning of the current approach, and not the wholesale abandonment of the style represented there. I need it to be creative, compelling and attention grabbing, but still professional. This should, at a minimum, update any places where the old name/logo is used, but I want the redesign to go beyond this to something more intuitive. I need high quality separate PNG files of the various logo styles for use in various documents, but HTML coding would be a helpful but not necessary addition.

Target Market(s)

People in need of cross-border tax services - Canada and US

Coding

Number of Pages Required

Requirements
Must have
• Greater crispness, sharpness - higher resolution
• A more compelling, organized approach - make the wording and images more accessible to the website user (especially the staff bios, which have scroll bars now)
Nice to have
• Replacement of stock image with a true image of the Halifax skyline
Should not have
• Deviate from colour pattern represented in website logo of blue/orange
• Deviate from existing logo except for word replacement

```html
<!DOCTYPE html>
<html lang="en">
<head>
<meta charset="utf-8">
<title>Brindlemoor Tax Advisory</title>
<link href="https://fonts.googleapis.com/css2?family=Roboto:wght@300;400;500;700&display=swap" rel="stylesheet">
<style>
:root{
  --orange:#f26522;
  --blue:#3a97d4;
  --blue-dark:#2c84c2;
  --ink:#333;
  --text:#666;
  --muted:#888;
  --grey-bg:#ececec;
  --footer:#555;
  --white:#fff;
}
*{box-sizing:border-box;margin:0;padding:0}
html,body{width:1200px;height:2308px;overflow:hidden}
body{position:relative;font-family:'Roboto',sans-serif;color:var(--text);background:var(--white)}
.abs{position:absolute}

/* hero */
.hero{left:0;top:0;width:1200px;height:615px;background:linear-gradient(180deg,#6b7280 0%,#8a8f96 25%,#7a6d62 55%,#3e3a36 80%,#2c3035 100%)}
.topbar{left:160px;top:4px;width:880px;height:28px;display:flex;align-items:center;color:#fff;font-size:12px;letter-spacing:1px}
.topbar .ph{display:flex;align-items:center;gap:8px;margin-right:18px}
.dot{width:22px;height:22px;border-radius:50%;background:var(--orange);display:inline-block}
.social{margin-left:auto;display:flex;gap:8px}
.navbar{left:160px;top:37px;width:880px;height:66px;background:#fff;display:flex;align-items:center;padding:0 14px}
.brand{display:flex;align-items:center;gap:8px}
.brand-mark{width:22px;height:22px;background:var(--blue)}
.brand-name{font-size:19px;font-weight:500;color:var(--ink);line-height:1}
.brand-line{font-size:8px;color:var(--muted);letter-spacing:1px;margin-top:4px}
.nav{margin-left:auto;display:flex;height:66px}
.nav a{display:flex;align-items:center;padding:0 12px;font-size:11px;color:#444;text-decoration:none;letter-spacing:.3px;position:relative}
.nav a.active{color:var(--orange)}
.nav a.active:after{content:"";position:absolute;left:12px;right:12px;bottom:0;height:3px;background:var(--orange)}
.hero-title{left:0;top:260px;width:1200px;text-align:center;color:#fff}
.hero-title .l1{font-size:43px;font-weight:300;letter-spacing:2px;line-height:48px}
.hero-title .l2{font-size:43px;font-weight:700;letter-spacing:1px;line-height:48px}
.slide-btn{top:271px;width:23px;height:83px;border:1px solid rgba(255,255,255,.7);color:#fff;font-size:10px;letter-spacing:3px;writing-mode:vertical-rl;text-align:center;display:flex;align-items:center;justify-content:center}

/* service panels */
.panel{top:512px;height:191px;color:#fff;display:flex;padding:28px 24px}
.panel.ind{left:161px;width:439px;background:var(--blue)}
.panel.paf{left:600px;width:438px;background:var(--blue-dark)}
.panel svg{flex:none;margin-right:22px;margin-top:14px}
.panel h3{font-size:17px;font-weight:400;letter-spacing:.5px;margin-bottom:10px}
.panel p{font-size:11px;line-height:16px}
.btn-line{display:inline-block;margin-top:12px;border:1px solid #fff;color:#fff;font-size:10px;padding:5px 9px;letter-spacing:.5px}

/* section heads */
.eyebrow{width:1200px;left:0;text-align:center;font-size:11px;letter-spacing:2px;color:var(--muted)}
.sect-title{width:1200px;left:0;text-align:center;font-size:24px;font-weight:500;letter-spacing:1px;color:var(--ink)}
.rule{left:520px;width:160px;height:1px;background:#ddd}
.rule:after{content:"";position:absolute;left:62px;width:36px;height:3px;top:-1px;background:var(--orange)}

.about-photo{left:161px;top:846px;width:428px;height:291px;background:linear-gradient(135deg,#e6ebef,#c7ccd2 50%,#5a6270)}
.about-text{left:618px;top:858px;width:420px}
.about-text h4{font-size:18px;font-weight:400;color:#555;margin-bottom:18px}
.about-text p{font-size:11.5px;line-height:21px;letter-spacing:.3px;margin-bottom:18px}

/* team */
.card{top:1458px;width:278px;height:329px;background:#fff;box-shadow:0 6px 22px rgba(0,0,0,.14)}
.portrait{top:1292px;width:224px;height:335px;background:linear-gradient(180deg,#3a3a3a,#262626)}
.card-body{top:1638px;width:278px;text-align:center;padding:0 22px}
.card-body h5{font-size:12.5px;font-weight:700;color:var(--ink);letter-spacing:.5px;margin-bottom:8px}
.card-body p{font-size:10.5px;line-height:15.5px;height:78px}
.btn-orange{display:inline-block;margin-top:16px;border:1px solid var(--orange);color:var(--orange);font-size:10px;padding:5px 10px;letter-spacing:.5px}

/* contact */
.contact-band{left:0;top:1846px;width:1200px;height:394px;background:var(--grey-bg)}
.contact-card{left:160px;top:1902px;width:352px;height:278px;background:#fff;box-shadow:0 2px 8px rgba(0,0,0,.1);padding:16px 12px}
.block-title{font-size:13px;font-weight:500;color:var(--ink);letter-spacing:.5px}
.block-title:after{content:"";display:block;width:36px;height:2px;background:var(--orange);margin-top:6px}
.c-row{display:flex;align-items:center;height:58px;border-bottom:1px solid #eee;font-size:10.5px;color:#555;line-height:15px}
.c-row:last-child{border-bottom:none}
.c-row svg{flex:none;margin:0 20px 0 6px}
.send{left:537px;top:1913px}
.field{background:#fff;font-size:10px;color:#555;padding:10px 6px;letter-spacing:.5px}
.submit{left:537px;top:2144px;width:89px;height:36px;background:var(--orange);color:#fff;font-size:10px;display:flex;align-items:center;justify-content:center;letter-spacing:.5px}

.footer{left:0;top:2240px;width:1200px;height:68px;background:var(--footer);color:#fff;font-size:9px;letter-spacing:.5px}
.footer span{position:absolute;top:30px}
</style>
</head>
<body>

<header>
  <div class="abs hero" role="img" aria-label="Photo of a harbour city skyline at dusk with waterfront buildings"></div>
  <div class="abs topbar">
    <span class="ph"><span class="dot"></span>(555) 014-2290</span>
    <span class="ph"><span class="dot"></span>(555) 014-2290</span>
    <span class="social"><span class="dot" style="width:18px;height:18px"></span><span class="dot" style="width:18px;height:18px"></span><span class="dot" style="width:18px;height:18px"></span></span>
  </div>
  <nav class="abs navbar">
    <div class="brand">
      <span class="brand-mark"></span>
      <div>
        <div class="brand-name">Brindlemoor Tax Advisory</div>
        <div class="brand-line">CROSS-BORDER TAX SERVICES • U.S. &amp; CANADA</div>
      </div>
    </div>
    <div class="nav">
      <a class="active">HOME</a><a>OUR TEAM</a><a>INDIVIDUALS</a><a>PUBLIC ACCOUNTING FIRMS</a><a>CONTACT</a><a>PAYMENT</a>
    </div>
  </nav>
  <div class="abs slide-btn" style="left:14px">PREV</div>
  <div class="abs slide-btn" style="left:1163px">NEXT</div>
  <div class="abs hero-title"><div class="l1">CROSS-BORDER TAX SERVICES</div><div class="l2">U.S. &amp; CANADA</div></div>
</header>

<section>
  <div class="abs panel ind">
    <svg width="120" height="120" viewBox="0 0 120 120" fill="none" stroke="#fff" stroke-width="7"><circle cx="60" cy="60" r="55"/><circle cx="60" cy="46" r="20"/><path d="M24 100c6-20 20-30 36-30s30 10 36 30"/></svg>
    <div><h3>FOR INDIVIDUALS</h3><p>We are firm devoted to helping individuals and businesses determine, comply with and minimize/optimize their Canadian and U.S. tax obligations. Let's take a moment to unpack that sentence.</p><span class="btn-line">LEARN MORE ➜</span></div>
  </div>
  <div class="abs panel paf">
    <svg width="112" height="110" viewBox="0 0 112 110" fill="none" stroke="#fff" stroke-width="6"><path d="M20 104V12h44v92M64 104V44h40v60H8"/><g fill="#fff" stroke="none"><rect x="30" y="24" width="9" height="9"/><rect x="46" y="24" width="9" height="9"/><rect x="30" y="44" width="9" height="9"/><rect x="46" y="44" width="9" height="9"/><rect x="30" y="64" width="9" height="9"/><rect x="46" y="64" width="9" height="9"/><rect x="76" y="58" width="9" height="9"/><rect x="76" y="76" width="9" height="9"/></g></svg>
    <div><h3>PUBLIC ACCOUNTING FIRMS</h3><p>We provide a range of services to Canadian public accounting firms (PAFs) to assist them in serving their clients.In general, our PAF clients are small firms which are not large enough</p><span class="btn-line">LEARN MORE ➜</span></div>
  </div>
</section>

<section>
  <div class="abs eyebrow" style="top:747px">LOREM IPSUM DOLOR SIT AMET</div>
  <div class="abs sect-title" style="top:765px">WHO WE ARE</div>
  <div class="abs rule" style="top:806px"></div>
  <div class="abs about-photo" role="img" aria-label="Photo of three advisors meeting at an office table"></div>
  <div class="abs about-text">
    <h4>Suspendisse at ligula sodales</h4>
    <p>Lorem ipsum dolor sit amet, consectetur adipiscing elit. Sed dignissim justo vel nibh sagittis, eu lobortis risus tempor. Nunc ultrices risus a luctus accumsan. Vivamus vitae justo auctor, convallis quam sed, tempus est. Aliquam et tortor faucibus, congue turpis sit amet, luctus est. Aenean fermentum metus et felis commodo malesuada at at diam. Sed convallis dignissim massa, quis auctor sem ultrices ut. Ut odio ex, tempor vitae gravida eget, posuere sed sem.</p>
    <p>Lorem ipsum dolor sit amet, consectetur adipiscing elit. Sed dignissim justo vel nibh sagittis, eu lobortis risus tempor. Nunc ultrices risus a luctus accumsan. Vivamus vitae justo auctor, convallis quam sed, tempus</p>
  </div>
</section>

<section>
  <div class="abs eyebrow" style="top:1183px">LOREM IPSUM DOLOR SIT AMET</div>
  <div class="abs sect-title" style="top:1202px">OUR TEAM</div>
  <div class="abs rule" style="top:1243px"></div>

  <div class="abs card" style="left:160px"></div>
  <div class="abs portrait" style="left:188px" role="img" aria-label="Portrait of a senior tax advisor in a dark suit"></div>
  <div class="abs card-body" style="left:160px"><h5>MARTIN K. ASHDALE, CPA, CGA, EA</h5><p>Martin has been practicing tax for over 17 years. Educated at Lakeshore University and Eastbrook College, he began his career in the Mississauga office of Harwick Lowe LLP in September 1998.</p><span class="btn-orange">LEARN MORE ➜</span></div>

  <div class="abs card" style="left:460px"></div>
  <div class="abs portrait" style="left:488px" role="img" aria-label="Portrait of a tax advisor in a suit and tie"></div>
  <div class="abs card-body" style="left:460px"><h5>COLIN WEXBURY, CPA, CA</h5><p>Colin has been practicing tax for over 7 years. Educated at Harbourview University, where he graduated summa cum laude in 2005, Colin began his career at Pellam &amp; Co.</p><span class="btn-orange">LEARN MORE ➜</span></div>

  <div class="abs card" style="left:760px"></div>
  <div class="abs portrait" style="left:788px" role="img" aria-label="Portrait of a team member in a white blouse"></div>
  <div class="abs card-body" style="left:760px"><h5>NORA E. ASHDALE</h5><p>Nora splits her time between Brindlemoor Tax Advisory and her part-time studies at Valleyview University, where she is pursuing a Bachelor of Business Administration degree.</p><span class="btn-orange">LEARN MORE ➜</span></div>
</section>

<section>
  <div class="abs contact-band"></div>
  <div class="abs contact-card">
    <div class="block-title">CONTACT INFORMATION</div>
    <div style="margin-top:6px">
      <div class="c-row"><svg width="26" height="26" viewBox="0 0 26 26"><circle cx="13" cy="13" r="13" fill="var(--orange)"/><path d="M13 6a5 5 0 0 0-5 5c0 4 5 9 5 9s5-5 5-9a5 5 0 0 0-5-5z" fill="#fff"/><circle cx="13" cy="11" r="2" fill="var(--orange)"/></svg><span>418 CEDARLINE AVENUE, UNIT 12<br>EASTPORT, NOVA SCOTIA&nbsp; B0X 1A0</span></div>
      <div class="c-row"><svg width="26" height="26" viewBox="0 0 26 26"><circle cx="13" cy="13" r="13" fill="var(--orange)"/><path d="M13 6a5 5 0 0 0-5 5c0 4 5 9 5 9s5-5 5-9a5 5 0 0 0-5-5z" fill="#fff"/><circle cx="13" cy="11" r="2" fill="var(--orange)"/></svg><span>57 MARDEN ROAD, UNIT 3<br>WESTHAVEN, NOVA SCOTIA B0Y 2C0</span></div>
      <div class="c-row"><svg width="26" height="26" viewBox="0 0 26 26"><circle cx="13" cy="13" r="13" fill="var(--orange)"/><path d="M9 7l3 0 1 3-2 1.5a8 8 0 0 0 3.5 3.5L16 13l3 1v3c0 1-1 1.5-2 1.5A11 11 0 0 1 7.5 9c0-1 .5-2 1.5-2z" fill="#fff"/></svg><span>(555) 014-2290</span></div>
      <div class="c-row"><svg width="26" height="26" viewBox="0 0 26 26"><circle cx="13" cy="13" r="13" fill="var(--orange)"/><rect x="7" y="10" width="12" height="9" rx="1" fill="#fff"/><rect x="10" y="7" width="6" height="4" fill="none" stroke="#fff" stroke-width="1.5"/></svg><span>(555) 014-2290</span></div>
    </div>
  </div>
  <div class="abs send block-title">SEND US A MESSAGE</div>
  <div class="abs field" style="left:537px;top:1969px;width:238px;height:32px">NAME</div>
  <div class="abs field" style="left:537px;top:2023px;width:238px;height:32px">PHONE</div>
  <div class="abs field" style="left:537px;top:2077px;width:238px;height:32px">EMAIL</div>
  <div class="abs field" style="left:798px;top:1969px;width:240px;height:140px">MESSAGE</div>
  <div class="abs submit">SUBMIT</div>
</section>

<footer class="abs footer">
  <span style="left:160px">COPYRIGHT © 2017 BRINDLEMOOR TAX ADVISORY INC.</span>
  <span style="right:160px">TERMS OF USE AND PRIVACY POLICY</span>
</footer>

</body>
</html>
```